Graphic Design Vendora Book Description

There is a book on Vendora that is my competitor that has a large graphic design as part of the description for the book and I want a similar thing for my book to make it stand out more.

My competitors book is here: https://www.vendora-shop.example/Tidal-Lore-Starters-Grasping-Overview/dp/K31RTWP704/

My book is here: https://www.vendora-shop.example/Tidal-Lore-Groundwork-Workings-Interlacing/dp/K7Q2FXH58C/

You can see the kind of thing I am looking for on the book listing but I have attached an image below.

Thanks

Colin

```html
<!DOCTYPE html>
<html lang="en">
<head>
<meta charset="utf-8">
<title>Quantum Physics – Book Description Graphic</title>
<link rel="stylesheet" href="https://fonts.googleapis.com/css2?family=Bebas+Neue&family=Teko:wght@500;600&family=Carlito&display=swap">
<style>
  :root {
    --yellow: #f5e829;
    --heading-yellow: #f7e21c;
    --ink: #1c1c1c;
    --space-deep: #0b1322;
    --space-mid: #1f3150;
    --earth-glow: #3d7fd0;
    --black: #000000;
    --white: #ffffff;
    --paper: #f4f4f0;
  }
  * { box-sizing: border-box; margin: 0; padding: 0; }
  html, body { width: 720px; height: 1200px; overflow: hidden; background: var(--white); }
  .canvas { position: relative; width: 720px; height: 1200px; }

  /* Hero */
  .hero {
    position: absolute; left: 73px; top: 55px; width: 574px; height: 355px;
    overflow: hidden;
  }
  .hero-backdrop {
    position: absolute; inset: 0;
    background:
      radial-gradient(circle at 105% 72%, #8a6a52 0, #4b3a36 16%, transparent 30%),
      radial-gradient(ellipse at 20% 20%, #2c3d5c 0, transparent 55%),
      linear-gradient(160deg, var(--space-mid), var(--space-deep) 70%);
  }
  .hero-title {
    position: absolute; left: 0; right: 0; top: 14px;
    text-align: center;
    font-family: "Teko", sans-serif; font-weight: 600;
    font-size: 30px; line-height: 26px; color: var(--heading-yellow);
  }
  .hero-books {
    position: absolute; left: 30px; top: 78px; width: 510px; height: 265px;
    background:
      linear-gradient(100deg, transparent 0 9%, var(--yellow) 9% 43%, transparent 43%),
      linear-gradient(90deg, transparent 0 45%, var(--paper) 45% 95%, transparent 95%);
    border-radius: 3px;
    opacity: 0.95;
  }

  /* Feature cards */
  .features {
    position: absolute; left: 73px; top: 425px; width: 574px;
    display: grid; grid-template-columns: repeat(4, 131px); column-gap: 16px;
  }
  .feature-card {
    position: relative; height: 131px; background: var(--yellow);
  }
  .feature-card .bar {
    position: absolute; width: 3px; background: var(--ink);
  }
  .feature-card .bar-top { top: 0; }
  .feature-card .bar-bottom { bottom: 0; height: 48px; }
  .feature-title {
    position: absolute; left: 15px; top: 46px;
    font-family: "Bebas Neue", sans-serif; font-size: 21px; line-height: 18px;
    color: var(--ink);
  }
  .feature-text {
    margin-top: 12px;
    font-family: "Carlito", sans-serif; font-size: 9.1px; line-height: 10.6px;
    color: var(--ink);
  }

  /* Discover banner */
  .discover {
    position: absolute; left: 73px; top: 774px; width: 574px; height: 355px;
    background: var(--black); overflow: hidden;
  }
  .discover-scene {
    position: absolute; left: 0; top: 0; width: 300px; height: 355px;
    background:
      radial-gradient(circle at 8% 50%, #d8ecff 0, var(--earth-glow) 14%, transparent 42%),
      radial-gradient(ellipse at 40% 115%, #2a5a8e 0, #10243f 45%, transparent 75%),
      linear-gradient(90deg, #0c1a30, var(--black));
  }
  .discover-book {
    position: absolute; left: 85px; top: 44px; width: 140px; height: 288px;
    background: linear-gradient(90deg, #d9cc18 0 8%, var(--yellow) 8%);
  }
  .discover-content {
    position: absolute; left: 292px; top: 48px;
    font-family: "Teko", sans-serif; color: var(--white);
  }
  .discover-heading {
    font-weight: 600; font-size: 30px; line-height: 25px; color: var(--heading-yellow);
  }
  .discover-list {
    list-style: none; margin-top: 22px;
    font-weight: 500; font-size: 15.5px; line-height: 17px;
  }
</style>
</head>
<body>
<main class="canvas">

  <section class="hero">
    <div class="hero-backdrop" role="img" aria-label="Deep space backdrop with a comet and a cratered planet"></div>
    <h1 class="hero-title">Embark on a Mind-Bending Journey<br>into the Realm of Quantum Physics</h1>
    <div class="hero-books" role="img" aria-label="Yellow Quantum Physics book, its back cover and an open copy showing the wave-particle duality chapter"></div>
  </section>

  <section class="features">
    <article>
      <div class="feature-card">
        <span class="bar bar-top" style="left:88px;height:26px"></span>
        <h2 class="feature-title">Accessible<br>Introduction</h2>
        <span class="bar bar-bottom" style="left:16px"></span>
      </div>
      <p class="feature-text">Designed for curious minds, this book provides an accessible introduction to the world of quantum physics. With a touch of humor and clear explanations, Elias Thorne makes complex theories approachable and engaging. Reviewers praise the book for its ability to simplify difficult concepts without losing depth, making it a perfect starting point for anyone new to quantum mechanics.</p>
    </article>
    <article>
      <div class="feature-card">
        <span class="bar bar-top" style="left:118px;height:35px"></span>
        <h2 class="feature-title">Philosophical<br>Implications</h2>
        <span class="bar bar-bottom" style="left:13px"></span>
      </div>
      <p class="feature-text">Explore the philosophical implications of quantum theory and its impact on our perception of reality. "Quantum Physics" not only explains the science but also invites readers to ponder its deeper meanings. The book's unique blend of physics and philosophy offers a comprehensive understanding of the universe, sparking curiosity and wonder in readers. Reviewers find this aspect particularly thought-provoking, adding a new dimension to their appreciation of quantum mechanics.</p>
    </article>
    <article>
      <div class="feature-card">
        <span class="bar bar-top" style="left:37px;height:46px"></span>
        <h2 class="feature-title">Fasinating<br>Journey</h2>
        <span class="bar bar-bottom" style="left:87px"></span>
      </div>
      <p class="feature-text">Embark on an exhilarating journey through the subatomic world with this comprehensive guide. From the fundamental principles of wave-particle duality to the mind-bending implications of quantum entanglement, this book covers it all. Reviewers highlight the book's engaging narrative and thought-provoking examples, which make the exploration of quantum mechanics both enlightening and enjoyable.</p>
    </article>
    <article>
      <div class="feature-card">
        <span class="bar bar-top" style="left:19px;height:46px"></span>
        <h2 class="feature-title">Practical<br>Experiments</h2>
        <span class="bar bar-bottom" style="left:101px"></span>
      </div>
      <p class="feature-text">Embark on an exhilarating journey through the subatomic world with this comprehensive guide. From the fundamental principles of wave-particle duality to the mind-bending implications of quantum entanglement, this book covers it all. Reviewers highlight the book's engaging narrative and thought-provoking examples, which make the exploration of quantum mechanics both enlightening and enjoyable.</p>
    </article>
  </section>

  <section class="discover">
    <div class="discover-scene" role="img" aria-label="Earth seen from orbit with a rising sun glow"></div>
    <div class="discover-book" role="img" aria-label="Standing yellow Quantum Physics book with atom symbol on the cover"></div>
    <div class="discover-content">
      <h2 class="discover-heading">What You will discover<br>Inside:</h2>
      <ul class="discover-list">
        <li>- The Foundations of Quantum Mechanics</li>
        <li>- Wave-Particle Duality Explained</li>
        <li>- The Nature of Quantum States</li>
        <li>- The Uncertainty Principle</li>
        <li>- Quantum Entanglement and Its Implications</li>
        <li>- Quantum Computing and Cryptography</li>
        <li>- The Mathematical Framework of Quantum Mechanics</li>
        <li>- Philosophical Implications of Quantum Theory</li>
        <li>- Practical Quantum Experiments to Try at Home</li>
        <li>- The Future of Quantum Technologies</li>
      </ul>
    </div>
  </section>

</main>
</body>
</html>
```